Professional Business Cards

We need a nice looking, profession and modern business card for our new company. Our logo is attatched

Target Market(s)

Young Professionals

Industry/Entity Type

Financial

Contact Information for Business Card

FRONT

Vardane Ledger Pty Ltd
Level 22, Harbour Point, 48 Wattlebrook Ave
Sydney NSW 2000
ABN : 47 318 905 226

Owen Hadley - Chief Operations Officer
P : 02 9173 5528
M: 0418 356 091
owen@vardaneledger,com

BACK

- Cryptocurrency Exchange Services
- Cryptocurrency Mining Operations
- Cryptocurrency Investment Fund Offering

Font styles to use
Sans Serif

Colors
0255a3
9d9d9d

```html
<!DOCTYPE html>
<html lang="en">
<head>
<meta charset="utf-8">
<title>Vardane Ledger – Business Card</title>
<link rel="stylesheet" href="https://fonts.googleapis.com/css2?family=Montserrat:wght@600;700&family=Open+Sans:wght@400;600;700&display=swap">
<style>
  :root {
    --brand-blue: #0255a3;
    --slate-grey: #6d6d72;
    --panel-light: #f3f3f3;
    --panel-shade: #e4e4e4;
    --ink-white: #ffffff;
    --ink-soft: #eeeeee;
    --page-bg: #e8e8ea;
  }
  * { margin: 0; padding: 0; box-sizing: border-box; }
  html, body {
    width: 1200px;
    height: 900px;
    overflow: hidden;
    background: var(--page-bg);
  }
  .card {
    position: absolute;
    left: 120px;
    top: 153px;
    width: 960px;
    height: 593px;
    overflow: hidden;
    box-shadow: 0 10px 30px rgba(0,0,0,0.18);
    font-family: "Open Sans", Arial, sans-serif;
    color: var(--ink-white);
  }
  .card-shapes {
    position: absolute;
    inset: 0;
    width: 100%;
    height: 100%;
  }
  .band-blue { fill: var(--brand-blue); }
  .band-grey { fill: var(--slate-grey); }
  .panel-light { fill: url(#panelFill); }

  .identity {
    position: absolute;
    right: 71px;
    top: 50px;
    text-align: right;
  }
  .identity .name {
    font-family: "Montserrat", Arial, sans-serif;
    font-weight: 600;
    font-size: 33px;
    letter-spacing: 2px;
    line-height: 1;
  }
  .identity .role {
    font-size: 22px;
    margin-top: 12px;
    line-height: 1.2;
  }
  .identity .email {
    font-size: 22px;
    margin-top: 20px;
    line-height: 1.2;
  }

  .brand {
    position: absolute;
    left: 190px;
    top: 268px;
    display: flex;
    align-items: center;
    gap: 22px;
  }
  .brand .brand-mark {
    width: 58px;
    height: 58px;
    background: var(--brand-blue);
  }
  .brand .brand-name {
    font-family: "Montserrat", Arial, sans-serif;
    font-weight: 700;
    font-size: 50px;
    letter-spacing: 1px;
    color: var(--brand-blue);
    line-height: 1;
  }

  .contact {
    position: absolute;
    right: 71px;
    top: 448px;
    text-align: right;
    font-size: 21px;
    line-height: 32px;
    color: var(--ink-soft);
  }
  .contact .phones { color: var(--ink-white); }
  .contact .label { font-weight: 700; }
  .contact .gap { display: inline-block; width: 8px; }

  .abn {
    position: absolute;
    left: 54px;
    top: 527px;
    font-size: 21px;
    line-height: 32px;
    color: var(--ink-soft);
  }
</style>
</head>
<body>
  <section class="card" aria-label="Vardane Ledger business card, front">
    <svg class="card-shapes" viewBox="0 0 652 403" preserveAspectRatio="none" aria-hidden="true">
      <defs>
        <linearGradient id="panelFill" x1="0" y1="0" x2="1" y2="1">
          <stop offset="0" stop-color="#f6f6f6"/>
          <stop offset="1" stop-color="#e6e6e6"/>
        </linearGradient>
      </defs>
      <rect class="band-blue" x="0" y="0" width="652" height="207"/>
      <rect class="band-grey" x="0" y="207" width="652" height="196"/>
      <polygon class="panel-light" points="37,207 180,67 252,142 652,142 652,287 272,287 180,349"/>
    </svg>

    <div class="identity">
      <p class="name">OWEN HADLEY</p>
      <p class="role">Chief Operations Officer</p>
      <p class="email">www.owen@vardaneledger.com</p>
    </div>

    <div class="brand">
      <span class="brand-mark"></span>
      <span class="brand-name">VARDANE LEDGER</span>
    </div>

    <div class="contact">
      <p class="phones"><span class="label">P:</span> 02 9173 5528 <span class="label">M:</span><span class="gap"></span> 0418 356 091</p>
      <p>Level22, Harbour Point,</p>
      <p>48 Wattlebrook Ave Sydney NSW 2000</p>
    </div>

    <p class="abn">ABN : 47 318 905 226</p>
  </section>
</body>
</html>
```